PowerPoint template for my training workshop business

I would like to have a PowerPoint template created using my logo and palette materials created by Brindlework. I train and facilitate workshops using PowerPoint in both corporate and public settings.

I have attached the original design elements to this request.

```html
<!DOCTYPE html>
<html lang="en">
<head>
<meta charset="utf-8">
<title>Marlowe Hart Coaching – Slide Template</title>
<link rel="stylesheet" href="https://fonts.googleapis.com/css2?family=Cinzel:wght@500;600;700&family=Montserrat:wght@400;500;600;700&display=swap">
<style>
:root{
  --bg:#c9c9cc;
  --orange:#f7931e;
  --amber:#fbb22a;
  --yellow:#fdc732;
  --ink:#141414;
  --ink-soft:#2a2a2e;
  --steel:#7f8397;
  --text:#8a8d9c;
  --plum:#5a1f3f;
  --white:#ffffff;
  --head:'Cinzel',serif;
  --body:'Montserrat',sans-serif;
}
*{box-sizing:border-box;margin:0;padding:0}
html,body{width:1200px;height:2451px;overflow:hidden;background:var(--bg)}
.sheet{position:relative;width:1200px;height:2451px;background:var(--bg);font-family:var(--body)}
.defs{position:absolute;width:0;height:0}
.slide{position:absolute;width:558px;height:314px;background:var(--white);overflow:hidden;box-shadow:0 6px 10px rgba(0,0,0,.25)}
.col-a{left:26px}.col-b{left:617px}
.row-1{top:31px}.row-2{top:377px}.row-3{top:723px}.row-4{top:1068px}.row-5{top:1414px}.row-6{top:1760px}.row-7{top:2105px}
.abs{position:absolute}
.fill{position:absolute;inset:0}
.heading{font-family:var(--head);font-weight:700;color:var(--ink);letter-spacing:.3px;position:absolute}
.heading .light{color:var(--white)}
.heading .warm{color:var(--orange)}
.band-title{left:52px;top:12px;font-size:19px}
.copy{position:absolute;font-family:var(--body);color:var(--text);font-size:6px;line-height:18px;text-align:justify}
.dots{position:absolute;font-size:0}
.dots i{display:inline-block;width:4px;height:4px;border-radius:50%;background:var(--orange);margin-right:2.5px}
.brand{position:absolute;font-family:var(--head);font-weight:600;color:var(--orange);line-height:1;white-space:nowrap}
.photo{position:absolute}

/* cover */
.cover .brand{left:0;width:540px;text-align:center;top:146px;font-size:26px}
.cover .site{position:absolute;right:-78px;top:150px;transform:rotate(-90deg);font-family:var(--head);font-size:5.5px;letter-spacing:2px;color:#555;width:180px;text-align:center}

/* master title */
.master .title{position:absolute;left:282px;top:128px;width:240px;text-align:center;font-family:var(--head);font-weight:700;color:var(--white);font-size:27px;line-height:30px}
.master .subtitle{position:absolute;left:282px;top:196px;width:260px;text-align:right;font-size:7px;letter-spacing:3px;color:var(--amber);font-family:var(--head)}
.master .brand{left:282px;width:240px;text-align:center;top:66px;font-size:13px}
.social{position:absolute;right:42px;top:270px;display:flex;gap:3px}
.social i{display:block;width:12px;height:12px;border-radius:50%;border:1px solid var(--white)}

/* timeline */
.tl-label{font-family:var(--head);font-weight:700;font-size:7.5px;fill:var(--ink)}
.tl-label.on-dark{fill:var(--white)}
.tl-step{font-family:var(--body);font-size:6.5px;fill:var(--text);font-weight:500}

/* three factor */
.factor-list{position:absolute;left:300px;top:112px;width:230px}
.factor{display:flex;align-items:flex-start;gap:14px;height:52px}
.factor .num{font-family:var(--head);font-weight:600;font-size:19px;color:var(--ink-soft);width:22px;line-height:20px}
.factor p{font-size:7px;line-height:14px;color:var(--ink-soft)}
.factor.accent .num,.factor.accent p{color:var(--orange)}

/* testimonials */
.t-card{position:absolute;width:80px;height:131px;background:var(--white);border:1px solid #9a9a9a;border-radius:0 0 16px 0;overflow:hidden}
.t-card p{font-size:5px;line-height:12px;color:var(--text);padding:16px 8px 0}
.t-card .stars{position:absolute;left:6px;bottom:27px;color:#ef4e23;font-size:9px;letter-spacing:1px}
.t-card .foot{position:absolute;left:0;right:0;bottom:0;height:24px;background:linear-gradient(90deg,#0c0c0c,#3a3a40);color:var(--white);font-family:var(--head);font-weight:700;font-size:7px;display:flex;align-items:center;justify-content:center}
.t-main{position:absolute;left:47px;top:78px;width:120px;height:179px;border-radius:28px 0 20px 0;background:linear-gradient(135deg,#0b0b0b 40%,#5a5c66);color:var(--white);padding:12px 18px}
.t-main h3{font-family:var(--head);font-size:20px;line-height:24px;font-weight:700}
.t-main .tag{font-size:9.5px;margin-top:2px}
.t-main p{font-size:6px;line-height:11px;margin-top:26px;font-weight:500}

/* chart */
.chart-label{position:absolute;width:120px;text-align:center;font-size:9px;font-weight:700;color:var(--ink);top:242px}
.chart-label small{display:block;font-size:6.5px;font-weight:400;color:var(--text);margin-top:6px}

/* about me */
.me-role{position:absolute;left:48px;top:119px;width:168px;text-align:center;font-size:5px;line-height:7px;color:rgba(255,255,255,.85)}
.portrait{position:absolute;left:225px;top:88px;width:106px;height:106px;border-radius:50%;border:3px solid var(--white);background:radial-gradient(circle at 50% 40%,#b9876a 0,#6b3b2c 45%,#2a1a18 100%)}
.about-me .brand{left:345px;top:128px;font-size:12px;color:var(--white)}
.label{position:absolute;font-family:var(--head);font-weight:700;font-size:8.5px;color:var(--ink)}
.skill{position:absolute;left:402px;width:133px}
.skill .track{height:6px;border-radius:3px;background:#dcdcdc;overflow:hidden}
.skill .bar{height:6px;border-radius:3px;background:linear-gradient(90deg,var(--yellow),var(--orange))}
.skill span{display:block;text-align:right;font-size:4.8px;color:var(--ink-soft);margin-top:4px}
.vline{position:absolute;left:382px;top:190px;height:100px;border-left:1.5px dotted var(--ink)}

/* projects */
.proj{position:absolute;display:flex;align-items:center;gap:16px}
.badge{width:38px;height:38px;border-radius:50%;background:var(--orange);display:flex;align-items:center;justify-content:center;flex:none}
.badge b{width:28px;height:28px;border-radius:50%;background:var(--ink);color:var(--white);font-size:11px;font-weight:700;display:flex;align-items:center;justify-content:center}
.proj p{font-size:7.5px;line-height:14px;color:var(--text);width:190px}

/* our coaching */
.step{position:absolute;left:293px;display:flex;align-items:center;gap:18px}
.step .badge{width:29px;height:29px}
.step .badge b{width:21px;height:21px;font-size:9px}
.step .badge.plum b{background:linear-gradient(135deg,var(--plum),#1c0c15)}
.step p{font-size:6.5px;line-height:15px;color:var(--steel);width:150px;font-weight:500}

/* quote */
.quote-frame{position:absolute;left:77px;top:46px;width:320px;height:214px;border:1px solid rgba(255,255,255,.9);border-radius:14px}
.quote-box{position:absolute;left:52px;top:72px;width:306px;height:196px;border-radius:16px;background:rgba(251,178,38,.85)}
.quote-mark{position:absolute;left:95px;top:98px;font-family:var(--head);font-size:62px;font-weight:700;color:var(--ink);line-height:1}
.quote-text{position:absolute;left:112px;top:140px;width:238px;font-size:13.5px;line-height:17px;color:var(--white);font-weight:500}
.quote-by{position:absolute;left:290px;top:237px;font-size:6.5px;color:var(--white);font-weight:600}

/* contact */
.contact-row{position:absolute;left:45px;display:flex;align-items:center;gap:16px;font-size:8px;color:var(--ink-soft);font-weight:500}
.contact-row svg{width:18px;height:18px;flex:none}
.contact .brand{left:300px;width:240px;text-align:center;top:152px;font-size:15px}
</style>
</head>
<body>
<div class="sheet">

<svg class="defs" aria-hidden="true">
  <defs>
    <linearGradient id="warm" x1="0" y1="0" x2="1" y2="0">
      <stop offset="0" stop-color="#f7931e"/><stop offset="1" stop-color="#fdc732"/>
    </linearGradient>
    <linearGradient id="warmV" x1="0" y1="1" x2="0" y2="0">
      <stop offset="0" stop-color="#f7931e"/><stop offset="1" stop-color="#fdc732"/>
    </linearGradient>
    <linearGradient id="night" x1="0" y1="0" x2="1" y2="1">
      <stop offset="0" stop-color="#0b0b0b"/><stop offset=".6" stop-color="#26262b"/><stop offset="1" stop-color="#6a6c78"/>
    </linearGradient>
    <linearGradient id="nightH" x1="0" y1="0" x2="1" y2="0">
      <stop offset="0" stop-color="#0b0b0b"/><stop offset="1" stop-color="#80838f"/>
    </linearGradient>
  </defs>
</svg>

<!-- 1 cover -->
<section class="slide cover col-a row-1">
  <div class="brand">MARLOWE HART COACHING</div>
  <div class="site">WWW.MARLOWEHARTCOACHING.COM</div>
</section>

<!-- 2 master slide -->
<section class="slide master col-b row-1">
  <svg class="fill" viewBox="0 0 558 314" aria-hidden="true">
    <rect width="558" height="314" fill="url(#warmV)"/>
    <path d="M122 314 V70 Q122 0 192 0 H558 V314 Z" fill="#0b0b0b"/>
  </svg>
  <div class="photo" role="img" aria-label="Photo of hands typing on a laptop at a white desk with notepad and coffee" style="left:41px;top:47px;width:161px;height:221px;border-radius:34px 0 34px 0;background:linear-gradient(135deg,#f2f2f2,#d8d8d8 55%,#9a9a9a)"></div>
  <div class="brand">MARLOWE HART COACHING</div>
  <div class="title">MASTER SLIDE PRESENTATION</div>
  <div class="subtitle">SUBTITLE GOES HERE</div>
  <div class="social"><i></i><i></i><i></i></div>
</section>

<!-- 3 about coaching -->
<section class="slide col-a row-2">
  <svg class="fill" viewBox="0 0 558 314" aria-hidden="true">
    <path d="M0 0 H512 Q512 50 462 50 H60 Q0 50 0 100 Z" fill="url(#warm)"/>
  </svg>
  <h2 class="heading band-title">ABOUT <span class="light">COACHING</span></h2>
  <p class="copy" style="left:32px;top:108px;width:240px">Lorem ipsum dolor sit amet, consectetuer adipiscing elit, sed diam nonummy nibh euismod tincidunt ut laoreet dolore magna aliquam erat volutpat. Ut wisi enim ad minim veniam, quis nostrud exerci tation ullamcorper suscipit lobortis nisl ut aliquip ex ea commodo consequat. Duis autem vel eum iriure dolor in hendrerit in vulputate velit esse molestie consequat, vel illum dolore eu feugiat nulla facilisis at vero eros et accumsan et iusto odio dignissim qui blandit praesent luptatum zzril delenit augue duis dolore te feugait nulla facilisi.</p>
  <div class="photo" role="img" aria-label="Photo of a team stacking hands together over a desk with papers and laptops" style="left:275px;top:70px;width:283px;height:244px;border-radius:40px 0 0 0;background:linear-gradient(135deg,#7a4a2c,#a7774f 45%,#5b3a28)"></div>
</section>

<!-- 4 timeline -->
<section class="slide col-b row-2">
  <svg class="fill" viewBox="0 0 558 314">
    <path d="M0 0 H512 Q512 50 462 50 H60 Q0 50 0 100 Z" fill="url(#warm)"/>
    <path d="M100 129 H400 A22.5 22.5 0 0 1 400 174 H205 A23 23 0 0 0 205 220 H470" fill="none" stroke="#f7931e" stroke-width="14"/>
    <path d="M400 129 A22.5 22.5 0 0 1 400 174 M205 174 A23 23 0 0 0 205 220" fill="none" stroke="#fff" stroke-width="1.2" stroke-dasharray="4 3"/>
    <polygon points="190,122 285,122 295,129 285,136 190,136 200,129" fill="url(#nightH)"/>
    <polygon points="400,167 272,167 262,174 272,181 400,181" fill="url(#nightH)"/>
    <polygon points="285,213 380,213 390,220 380,227 285,227 295,220" fill="url(#nightH)"/>
    <circle cx="88" cy="129" r="20" fill="#f7931e"/><circle cx="88" cy="129" r="15" fill="url(#night)"/>
    <circle cx="482" cy="220" r="20" fill="#f7931e"/><circle cx="482" cy="220" r="15" fill="url(#night)"/>
    <text x="88" y="132" text-anchor="middle" class="tl-label on-dark">START</text>
    <text x="482" y="223" text-anchor="middle" class="tl-label on-dark" style="font-size:6.5px">FINISH</text>
    <text x="140" y="132" text-anchor="middle" class="tl-label">JAN</text>
    <text x="242" y="132" text-anchor="middle" class="tl-label on-dark">MAR</text>
    <text x="340" y="132" text-anchor="middle" class="tl-label">APR</text>
    <text x="330" y="177" text-anchor="middle" class="tl-label on-dark">JUN</text>
    <text x="232" y="177" text-anchor="middle" class="tl-label">AUG</text>
    <text x="245" y="223" text-anchor="middle" class="tl-label">SEP</text>
    <text x="338" y="223" text-anchor="middle" class="tl-label on-dark">NOV</text>
    <text x="430" y="223" text-anchor="middle" class="tl-label">DEC</text>
    <text x="138" y="116" text-anchor="middle" class="tl-step">Step 1</text>
    <text x="240" y="116" text-anchor="middle" class="tl-step">Step 2</text>
    <text x="338" y="116" text-anchor="middle" class="tl-step">Step 3</text>
    <text x="328" y="161" text-anchor="middle" class="tl-step">Step 4</text>
    <text x="230" y="161" text-anchor="middle" class="tl-step">Step 5</text>
    <text x="230" y="238" text-anchor="middle" class="tl-step">Step 5</text>
    <text x="330" y="238" text-anchor="middle" class="tl-step">Step 5</text>
    <text x="428" y="238" text-anchor="middle" class="tl-step">Step 5</text>
  </svg>
  <h2 class="heading band-title">TIME LINE</h2>
</section>

<!-- 5 three factor -->
<section class="slide col-a row-3">
  <svg class="fill" viewBox="0 0 558 314">
    <path d="M0 0 H512 Q512 50 462 50 H60 Q0 50 0 100 Z" fill="url(#warm)"/>
    <circle cx="147" cy="150" r="45" fill="url(#night)"/>
    <circle cx="110" cy="220" r="45" fill="url(#warm)"/>
    <circle cx="189" cy="222" r="45" fill="#7f8397"/>
    <text x="147" y="161" text-anchor="middle" font-family="Cinzel,serif" font-weight="700" font-size="32" fill="#fff">01</text>
    <text x="110" y="231" text-anchor="middle" font-family="Cinzel,serif" font-weight="700" font-size="32" fill="#fff">02</text>
    <text x="193" y="233" text-anchor="middle" font-family="Cinzel,serif" font-weight="700" font-size="32" fill="#fff">03</text>
  </svg>
  <h2 class="heading band-title">THREE FACTOR</h2>
  <div class="factor-list">
    <div class="factor"><span class="num">01</span><p>Lorem Ipsum is simply dummy text of the printing and typesetting industry</p></div>
    <div class="factor accent"><span class="num">02</span><p>Lorem Ipsum is simply dummy text of the printing and typesetting industry</p></div>
    <div class="factor"><span class="num">03</span><p>Lorem Ipsum is simply dummy text of the printing and typesetting industry</p></div>
  </div>
</section>

<!-- 6 testimonials -->
<section class="slide col-b row-3">
  <svg class="fill" viewBox="0 0 558 314">
    <path d="M0 0 H465 Q465 55 410 55 H150 Q95 55 95 110 V314 H0 Z" fill="url(#warmV)"/>
    <g fill="none" stroke="#888" stroke-width="1">
      <path d="M181 92 H470 Q480 92 480 102 V113"/>
      <path d="M181 119 H345 Q355 119 355 129 V140"/>
      <path d="M181 146 H228 Q238 146 238 156 V166"/>
    </g>
    <circle cx="181" cy="92" r="5" fill="#222"/>
    <circle cx="181" cy="119" r="5" fill="#222"/>
    <circle cx="181" cy="146" r="5" fill="#222"/>
  </svg>
  <div class="t-main">
    <h3>TITLE<br>SLIDE</h3>
    <div class="tag">(Testimonials)</div>
    <p>Lorem Ipsum is simply dummy text of the printing and typesetting industry</p>
  </div>
  <div class="t-card" style="left:193px;top:166px"><p>Lorem Ipsum is simply dummy text of the printing and typesetting industry</p><span class="stars">★★★★★</span><div class="foot">LOREM IPSUM</div></div>
  <div class="t-card" style="left:313px;top:140px"><p>Lorem Ipsum is simply dummy text of the printing and typesetting industry</p><span class="stars">★★★★★</span><div class="foot">LOREM IPSUM</div></div>
  <div class="t-card" style="left:427px;top:113px"><p>Lorem Ipsum is simply dummy text of the printing and typesetting industry</p><span class="stars">★★★★★</span><div class="foot">LOREM IPSUM</div></div>
</section>

<!-- 7 chart -->
<section class="slide col-a row-4">
  <svg class="fill" viewBox="0 0 558 314">
    <path d="M0 0 H512 Q512 50 462 50 H60 Q0 50 0 100 Z" fill="url(#warm)"/>
    <g>
      <ellipse cx="119" cy="224" rx="48" ry="5" fill="#eee"/>
      <circle cx="119" cy="159" r="49" fill="none" stroke="#e2e2e2" stroke-width="12"/>
      <circle cx="119" cy="159" r="49" fill="none" stroke="#f7931e" stroke-width="12" stroke-dasharray="166.3 307.9" transform="rotate(-90 119 159)"/>
      <circle cx="119" cy="159" r="41" fill="url(#night)"/>
      <text x="119" y="167" text-anchor="middle" font-family="Cinzel,serif" font-weight="700" font-size="23" fill="#fff">54%</text>
    </g>
    <g>
      <ellipse cx="271" cy="224" rx="48" ry="5" fill="#eee"/>
      <circle cx="271" cy="159" r="49" fill="none" stroke="#e2e2e2" stroke-width="12"/>
      <circle cx="271" cy="159" r="49" fill="none" stroke="url(#warm)" stroke-width="12" stroke-dasharray="230.9 307.9" transform="rotate(-90 271 159)"/>
      <circle cx="271" cy="159" r="41" fill="url(#night)"/>
      <text x="271" y="167" text-anchor="middle" font-family="Cinzel,serif" font-weight="700" font-size="23" fill="#fff">75%</text>
    </g>
    <g>
      <ellipse cx="430" cy="224" rx="48" ry="5" fill="#eee"/>
      <circle cx="430" cy="159" r="49" fill="none" stroke="#e2e2e2" stroke-width="12"/>
      <circle cx="430" cy="159" r="49" fill="none" stroke="url(#warm)" stroke-width="12" stroke-dasharray="277.1 307.9" transform="rotate(-90 430 159)"/>
      <circle cx="430" cy="159" r="41" fill="url(#night)"/>
      <text x="430" y="167" text-anchor="middle" font-family="Cinzel,serif" font-weight="700" font-size="23" fill="#fff">90%</text>
    </g>
  </svg>
  <h2 class="heading band-title">GRAPHIC CHART</h2>
  <div class="chart-label" style="left:59px">Lorem ipsum<small>dolor sit amet,</small></div>
  <div class="chart-label" style="left:211px">Lorem ipsum<small>dolor sit amet,</small></div>
  <div class="chart-label" style="left:370px">Lorem ipsum<small>dolor sit amet,</small></div>
</section>

<!-- 8 mission -->
<section class="slide col-b row-4">
  <div class="photo" role="img" aria-label="Photo of a modern grey bedroom seen through sliding glass doors" style="left:0;top:0;width:558px;height:146px;background:linear-gradient(90deg,#6e6e6c,#a9a8a4 40%,#c9c7c2 60%,#5e5d5b)"></div>
  <svg class="abs" style="left:0;top:146px" width="558" height="168" viewBox="0 0 558 168" aria-hidden="true">
    <rect width="558" height="168" fill="url(#warmV)"/>
    <path d="M120 0 H558 V168 H170 Q120 168 120 118 Z" fill="#fff"/>
  </svg>
  <h2 class="heading" style="left:18px;top:186px;font-size:18px;line-height:20px">MY<br><span class="light">MISSION</span></h2>
  <div class="dots" style="left:19px;top:233px"><i style="background:var(--ink)"></i><i style="background:var(--ink)"></i><i style="background:var(--ink)"></i><i style="background:var(--ink)"></i></div>
  <p class="copy" style="left:168px;top:178px;width:356px;line-height:14.5px;font-size:6px">Lorem ipsum dolor sit amet, consectetuer adipiscing elit, sed diam nonummy nibh euismod tincidunt ut laoreet dolore magna aliquam erat volutpat. Ut wisi enim ad minim veniam, quis nostrud exerci tation ullamcorper suscipit lobortis nisl ut aliquip ex ea commodo consequat. Duis autem vel eum iriure dolor in hendrerit in vulputate velit esse molestie consequat, vel illum dolore eu feugiat nulla facilisis at vero eros et accumsan et iusto odio dignissim qui blandit praesent luptatum zzril delenit augue duis dolore te feugait nulla facilisi.</p>
</section>

<!-- 9 about me -->
<section class="slide about-me col-a row-5">
  <svg class="fill" viewBox="0 0 558 314" aria-hidden="true">
    <rect width="558" height="314" fill="url(#warm)"/>
    <path d="M0 314 V210 Q0 150 60 150 H500 Q558 150 558 92 V314 Z" fill="#fff"/>
  </svg>
  <h2 class="heading" style="left:0;width:558px;text-align:center;top:17px;font-size:18px">ABOUT ME</h2>
  <div class="dots" style="left:268px;top:44px"><i style="background:var(--white)"></i><i style="background:var(--white)"></i><i style="background:var(--white)"></i><i style="background:var(--white)"></i></div>
  <p class="me-role">Workshop facilitator and learning program lead – Northwind Health: team growth &amp; training</p>
  <div class="portrait" role="img" aria-label="Portrait photo of the coach"></div>
  <div class="brand">MARLOWE HART COACHING</div>
  <span class="label" style="left:340px;top:182px">BIO</span>
  <p class="copy" style="left:36px;top:195px;width:321px;line-height:14.5px;color:#6e7182;font-weight:600">Lorem ipsum dolor sit amet, consectetuer adipiscing elit, sed diam nonummy nibh euismod tincidunt ut laoreet dolore magna aliquam erat volutpat. Ut wisi enim ad minim veniam, quis nostrud exerci tation ullamcorper suscipit lobortis nisl ut aliquip ex ea commodo consequat. Duis autem vel eum iriure dolor in hendrerit in vulputate velit esse molestie consequat, vel illum dolore eu feugiat nulla facilisis at vero eros et accumsan et iusto odio dignissim qui blandit praesent luptatum zzril delenit augue duis dolore te feugait nulla facilisi.</p>
  <span class="vline"></span>
  <span class="label" style="left:498px;top:182px">SKILLS</span>
  <div class="skill" style="top:197px"><div class="track"><div class="bar" style="width:78%"></div></div><span>Lorem ipsum dolor sit</span></div>
  <div class="skill" style="top:220px"><div class="track"><div class="bar" style="width:70%"></div></div><span>Lorem ipsum dolor sit</span></div>
  <div class="skill" style="top:243px"><div class="track"><div class="bar" style="width:88%"></div></div><span>Lorem ipsum dolor sit</span></div>
  <div class="skill" style="top:266px"><div class="track"><div class="bar" style="width:94%"></div></div><span>Lorem ipsum dolor sit</span></div>
</section>

<!-- 10 projects -->
<section class="slide col-b row-5">
  <svg class="fill" viewBox="0 0 558 314">
    <path d="M0 0 H120 Q235 60 232 160 Q228 262 160 314 H0 Z" fill="url(#warmV)"/>
  </svg>
  <div class="photo" role="img" aria-label="Photo of a presenter with a tablet leading a meeting around a table" style="left:0;top:0;width:215px;height:314px;clip-path:path('M0 0 H100 Q215 60 214 160 Q210 262 140 314 H0 Z');background:linear-gradient(135deg,#4a3c30,#7c6a58 50%,#3a3530)"></div>
  <h2 class="heading" style="left:19px;top:98px;font-size:18px;line-height:21px;color:var(--white)">MY<br>PROJECTS</h2>
  <div class="dots" style="left:20px;top:143px"><i style="background:var(--white)"></i><i style="background:var(--white)"></i><i style="background:var(--white)"></i><i style="background:var(--white)"></i></div>
  <div class="proj" style="left:251px;top:17px"><span class="badge"><b>01</b></span><p>Lorem Ipsum is simply dummy text of the printing and typesetting industry</p></div>
  <div class="proj" style="left:281px;top:93px"><span class="badge"><b>02</b></span><p>Lorem Ipsum is simply dummy text of the printing and typesetting industry</p></div>
  <div class="proj" style="left:281px;top:176px"><span class="badge"><b>03</b></span><p>Lorem Ipsum is simply dummy text of the printing and typesetting industry</p></div>
  <div class="proj" style="left:251px;top:259px"><span class="badge"><b>04</b></span><p>Lorem Ipsum is simply dummy text of the printing and typesetting industry</p></div>
</section>

<!-- 11 section one -->
<section class="slide col-a row-6">
  <svg class="fill" viewBox="0 0 558 314" aria-hidden="true">
    <path d="M400 0 H558 V314 H438 V50 Q438 0 400 0 Z" fill="url(#warmV)"/>
  </svg>
  <h2 class="heading" style="left:25px;top:50px;font-size:18px">SECTION <span class="warm">ONE</span></h2>
  <div class="dots" style="left:26px;top:76px"><i></i><i></i><i></i><i></i></div>
  <p class="copy" style="left:25px;top:96px;width:275px;line-height:14.5px;font-size:6px">Lorem ipsum dolor sit amet, consectetuer adipiscing elit, sed diam nonummy nibh euismod tincidunt ut laoreet dolore magna aliquam erat volutpat. Ut wisi enim ad minim veniam, quis nostrud exerci tation ullamcorper suscipit lobortis nisl ut aliquip ex ea commodo consequat. Duis autem vel eum iriure dolor in hendrerit in vulputate velit esse molestie consequat, vel illum dolore eu feugiat nulla facilisis at vero eros et accumsan et iusto odio dignissim qui blandit praesent luptatum zzril delenit augue duis dolore te feugait nulla facilisi.</p>
  <div class="brand" style="left:27px;top:263px;font-size:9px">MARLOWE HART COACHING</div>
  <div class="photo" role="img" aria-label="Photo of smiling women in a casual meeting with coffee cups" style="left:362px;top:55px;width:159px;height:221px;border-radius:30px 0 30px 0;background:linear-gradient(135deg,#c9cdc6,#8c7a62 50%,#4e4a3e);box-shadow:0 6px 12px rgba(0,0,0,.3)"></div>
</section>

<!-- 12 our coaching -->
<section class="slide col-b row-6">
  <h2 class="heading" style="left:36px;top:36px;font-size:19px;line-height:23px"><span class="warm">OUR</span><br>COACHING</h2>
  <div class="abs" style="left:38px;top:91px;font-family:var(--head);font-size:7px;letter-spacing:3.5px;color:var(--ink);font-weight:600">SUBTITLE GOES HERE</div>
  <p class="copy" style="left:38px;top:142px;width:204px;line-height:14.5px;font-size:6px;color:#6e7182;font-weight:600">Lorem ipsum dolor sit amet, consectetuer adipiscing elit, sed diam nonummy nibh euismod tincidunt ut laoreet dolore magna aliquam erat volutpat. Ut wisi enim ad minim veniam, quis nostrud exerci tation ullamcorper suscipit lobortis nisl ut aliquip ex ea commodo consequat.</p>
  <span class="abs" style="left:307px;top:38px;width:3px;height:256px;background:#9a9cab"></span>
  <div class="step" style="top:62px"><span class="badge"><b>01</b></span><p>Lorem Ipsum is simply dummy text of the printing and typesetting industry</p></div>
  <div class="step" style="top:121px"><span class="badge plum"><b>02</b></span><p>Lorem Ipsum is simply dummy text of the printing and typesetting industry</p></div>
  <div class="step" style="top:181px"><span class="badge"><b>03</b></span><p>Lorem Ipsum is simply dummy text of the printing and typesetting industry</p></div>
  <div class="step" style="top:240px"><span class="badge"><b>04</b></span><p>Lorem Ipsum is simply dummy text of the printing and typesetting industry</p></div>
</section>

<!-- 13 quote -->
<section class="slide col-a row-7">
  <div class="photo fill" role="img" aria-label="Photo of a group of friends embracing on a hilltop at sunset" style="background:linear-gradient(180deg,#c9c2c6 0%,#b8a79c 45%,#a2773f 75%,#4a3518 100%)"></div>
  <div class="quote-frame"></div>
  <div class="quote-box"></div>
  <div class="quote-mark">“</div>
  <p class="quote-text">Lorem ipsum dolor sit amet, consectetuer adipiscing elit, sed diam nonummy nibh euismod tincidunt</p>
  <div class="quote-by">-Lorem ipsum</div>
</section>

<!-- 14 contact -->
<section class="slide contact col-b row-7">
  <h2 class="heading" style="left:30px;top:118px;font-size:18px">CONTACT</h2>
  <div class="dots" style="left:31px;top:144px"><i></i><i></i><i></i><i></i></div>
  <div class="contact-row" style="top:176px">
    <svg viewBox="0 0 20 20" fill="none" stroke="#f7931e" stroke-width="1.3"><circle cx="10" cy="10" r="8"/><ellipse cx="10" cy="10" rx="3.5" ry="8"/><path d="M2 10H18M3.5 6H16.5M3.5 14H16.5"/></svg>
    <span>www.marlowehartcoaching.com</span>
  </div>
  <div class="contact-row" style="top:209px">
    <svg viewBox="0 0 20 20" fill="none" stroke="#f7931e" stroke-width="1.3"><path d="M4 2.5L7.5 2l2 4.5-2 1.5c1 2.5 2.5 4 5 5l1.5-2 4.5 2-.5 3.5C10 17 3 10 4 2.5Z"/></svg>
    <span>555-014-2290</span>
  </div>
  <div class="contact-row" style="top:240px">
    <svg viewBox="0 0 20 20" fill="none" stroke="#f7931e" stroke-width="1.3"><rect x="2" y="4.5" width="16" height="11"/><path d="M2 4.5l8 6.5 8-6.5"/></svg>
    <span>hello@marlowehartcoaching.com</span>
  </div>
  <div class="contact-row" style="top:270px">
    <svg viewBox="0 0 20 20" fill="none" stroke="#f7931e" stroke-width="1.3"><path d="M10 18s-5.5-5.5-5.5-9.5a5.5 5.5 0 0 1 11 0C15.5 12.5 10 18 10 18Z"/><circle cx="10" cy="8.5" r="2"/></svg>
    <span>Located in the Riverton/Lakeshore, Westland area.</span>
  </div>
  <div class="brand">MARLOWE HART COACHING</div>
</section>

</div>
</body>
</html>
```